Visitenkarten-Design für italienisches Küchenschiff
Zielgruppe
Restaurantschiff Morvella
Aufgabenstellung
Wir sind ein italienische Küche Schiff auf der Binnenalster in Hamburg und wollen den schönen Blick und gerne auch die italienischen Farben widerspiegeln...ich brauche das einmal neutral für den normalen Gast....und würde das denn..wenn es denn gut wird...auch gerne individell mit m e i n e r Tel Nr und auch für meine führenden Mitarbeiter personalisieren...aber...zuerst natürlich das neutrale...dazu schicke ich die alte Karte mit dem auch alten Logo was nicht unbedingt verwendet werden muss...

```html
<!DOCTYPE html>
<html lang="de">
<head>
<meta charset="utf-8">
<title>Morvella – Visitenkarten</title>
<link rel="stylesheet" href="https://fonts.googleapis.com/css2?family=Saira+Condensed:wght@300&display=swap">
<style>
  :root {
    --stage: #4a4a4a;
    --card-dark: #333333;
    --card-light: #ffffff;
    --taupe: #8a7d6e;
    --taupe-deep: #7a6e60;
    --graphite: #444444;
    --rule: #d9d4cd;
    --rule-dark: #4a4745;
    --it-green: #0a9150;
    --it-white: #ffffff;
    --it-silver: #c8c8c8;
    --it-red: #a52a32;
  }
  * { margin: 0; padding: 0; box-sizing: border-box; }
  html, body { width: 1200px; height: 1200px; overflow: hidden; background: var(--stage); }
  body { position: relative; font-family: "Saira Condensed", "Arial Narrow", sans-serif; font-weight: 300; }

  .card {
    position: absolute; width: 510px; height: 328px;
    box-shadow: 3px 4px 6px rgba(0,0,0,0.45);
    overflow: hidden;
  }
  .card--front { left: 61px; }
  .card--back { left: 628px; }
  .row-1 { top: 30px; }
  .row-2 { top: 436px; }
  .row-3 { top: 842px; }

  .theme-dark { background: var(--card-dark); --ink: var(--taupe); --divider: var(--rule-dark); --mid-band: var(--it-white); }
  .theme-warm { background: var(--card-light); --ink: var(--taupe-deep); --divider: var(--rule); --mid-band: var(--it-silver); }
  .theme-mono { background: var(--card-light); --ink: var(--graphite); --divider: var(--rule); --mid-band: var(--it-silver); }

  .text { position: absolute; color: var(--ink); white-space: nowrap; line-height: 1; }

  /* front */
  .brand { position: absolute; left: 25px; top: 178px; display: flex; align-items: center; gap: 10px; }
  .brand__name { font-size: 40px; color: var(--ink); letter-spacing: 1px; line-height: 1; }
  .brand__dot { width: 14px; height: 14px; border-radius: 50%; background: var(--ink); }
  .divider { position: absolute; left: 251px; top: 63px; width: 1px; height: 236px; background: var(--divider); }
  .address, .contact { position: absolute; left: 269px; color: var(--ink); font-size: 17px; line-height: 23.6px; }
  .address { top: 60px; }
  .contact__title { position: absolute; left: 269px; top: 139px; font-size: 21px; color: var(--ink); }
  .contact { top: 166px; }
  .contact .label { display: inline-block; width: 32px; }

  /* back */
  .photo { position: absolute; left: 22px; width: 211px; }
  .photo--cabin {
    top: 20px; height: 129px;
    background: linear-gradient(180deg, #7a5a3a 0%, #8aa1b6 18%, #5b6f78 45%, #a43a36 68%, #e8e6e2 82%, #d8d4cf 100%);
  }
  .photo--harbour {
    top: 163px; height: 126px;
    background: linear-gradient(180deg, #6b5a6e 0%, #7c6474 35%, #4c4550 62%, #c9b28a 72%, #2a2a34 82%, #1d1f28 100%);
  }
  .heading { font-size: 21px; }
  .line { font-size: 17px; }
  .band { position: absolute; left: 0; top: 301px; width: 510px; height: 9px; display: flex; }
  .band span { flex: 1; }
  .band .green { background: var(--it-green); }
  .band .white { background: var(--mid-band); }
  .band .red { background: var(--it-red); }
</style>
</head>
<body>

<!-- Variante 1: dunkel -->
<section class="card card--front row-1 theme-dark">
  <div class="brand"><span class="brand__name">MORVELLA</span><span class="brand__dot"></span></div>
  <div class="divider"></div>
  <p class="address">Schiffsrestaurant Morvella<br>Seekai (Wasserseite)<br>20095 Hamburg</p>
  <p class="contact__title">Kontakt</p>
  <p class="contact"><span class="label">Tel:</span>+49 040 / 55 01 23<br><span class="label">Fax:</span>+49 040 / 55 01 2<br>www.kanalschiff-morvella.de<br>E-Mail: info(at)kanalschiff-morvella.de</p>
</section>
<section class="card card--back row-1 theme-dark">
  <div class="photo photo--cabin" role="img" aria-label="Foto: gedeckte Tische im Schiffssalon mit Blick aufs Wasser"></div>
  <div class="photo photo--harbour" role="img" aria-label="Foto: beleuchtete Uferpromenade bei Nacht"></div>
  <span class="text heading" style="left:257px;top:63px">Öffnungszeiten</span>
  <span class="text line" style="left:257px;top:87px">Montag - Sonntag</span>
  <span class="text line" style="left:384px;top:87px">12:00 - 23:00</span>
  <span class="text line" style="left:370px;top:108px">Küche bis 22:00</span>
  <span class="text line" style="left:257px;top:129px">Sonntags haben wir derzeit geöffnet.</span>
  <span class="text heading" style="left:257px;top:177px">Reservierungen</span>
  <span class="text line" style="left:257px;top:200px">Wollen Sie einen Tisch reservieren? Wir</span>
  <span class="text line" style="left:257px;top:222px">freuen uns auf Ihren Anruf oder eine:</span>
  <span class="text line" style="left:257px;top:243px">reservierung(at)kanalschiff-morvella.de</span>
  <div class="band"><span class="green"></span><span class="white"></span><span class="red"></span></div>
</section>

<!-- Variante 2: hell, warm -->
<section class="card card--front row-2 theme-warm">
  <div class="brand"><span class="brand__name">MORVELLA</span><span class="brand__dot"></span></div>
  <div class="divider"></div>
  <p class="address">Schiffsrestaurant Morvella<br>Seekai (Wasserseite)<br>20095 Hamburg</p>
  <p class="contact__title">Kontakt</p>
  <p class="contact"><span class="label">Tel:</span>+49 040 / 55 01 23<br><span class="label">Fax:</span>+49 040 / 55 01 2<br>www.kanalschiff-morvella.de<br>E-Mail: info(at)kanalschiff-morvella.de</p>
</section>
<section class="card card--back row-2 theme-warm">
  <div class="photo photo--cabin" role="img" aria-label="Foto: gedeckte Tische im Schiffssalon mit Blick aufs Wasser"></div>
  <div class="photo photo--harbour" role="img" aria-label="Foto: beleuchtete Uferpromenade bei Nacht"></div>
  <span class="text heading" style="left:257px;top:63px">Öffnungszeiten</span>
  <span class="text line" style="left:257px;top:87px">Montag - Sonntag</span>
  <span class="text line" style="left:384px;top:87px">12:00 - 23:00</span>
  <span class="text line" style="left:370px;top:108px">Küche bis 22:00</span>
  <span class="text line" style="left:257px;top:129px">Sonntags haben wir derzeit geöffnet.</span>
  <span class="text heading" style="left:257px;top:177px">Reservierungen</span>
  <span class="text line" style="left:257px;top:200px">Wollen Sie einen Tisch reservieren? Wir</span>
  <span class="text line" style="left:257px;top:222px">freuen uns auf Ihren Anruf oder eine:</span>
  <span class="text line" style="left:257px;top:243px">reservierung(at)kanalschiff-morvella.de</span>
  <div class="band"><span class="green"></span><span class="white"></span><span class="red"></span></div>
</section>

<!-- Variante 3: hell, graphit -->
<section class="card card--front row-3 theme-mono">
  <div class="brand"><span class="brand__name">MORVELLA</span><span class="brand__dot"></span></div>
  <div class="divider"></div>
  <p class="address">Schiffsrestaurant Morvella<br>Seekai (Wasserseite)<br>20095 Hamburg</p>
  <p class="contact__title">Kontakt</p>
  <p class="contact"><span class="label">Tel:</span>+49 040 / 55 01 23<br><span class="label">Fax:</span>+49 040 / 55 01 2<br>www.kanalschiff-morvella.de<br>E-Mail: info(at)kanalschiff-morvella.de</p>
</section>
<section class="card card--back row-3 theme-mono">
  <div class="photo photo--cabin" role="img" aria-label="Foto: gedeckte Tische im Schiffssalon mit Blick aufs Wasser"></div>
  <div class="photo photo--harbour" role="img" aria-label="Foto: beleuchtete Uferpromenade bei Nacht"></div>
  <span class="text heading" style="left:257px;top:63px">Öffnungszeiten</span>
  <span class="text line" style="left:257px;top:87px">Montag - Sonntag</span>
  <span class="text line" style="left:384px;top:87px">12:00 - 23:00</span>
  <span class="text line" style="left:370px;top:108px">Küche bis 22:00</span>
  <span class="text line" style="left:257px;top:129px">Sonntags haben wir derzeit geöffnet.</span>
  <span class="text heading" style="left:257px;top:177px">Reservierungen</span>
  <span class="text line" style="left:257px;top:200px">Wollen Sie einen Tisch reservieren? Wir</span>
  <span class="text line" style="left:257px;top:222px">freuen uns auf Ihren Anruf oder eine:</span>
  <span class="text line" style="left:257px;top:243px">reservierung(at)kanalschiff-morvella.de</span>
  <div class="band"><span class="green"></span><span class="white"></span><span class="red"></span></div>
</section>

</body>
</html>
```